Webdesign für Kirchen-Gemeinde
Zielgruppe
freie, kleine Kirchen-Gemeinde, protestantisch, Zielgruppe an der Bibel und Religion und Weltgeschehen Interessierte
Aufgabenstellung
Es besteht bereits eine Webseite, die aber vom Design her aufgepeppt werden soll. Ein entsprechender Vorschlag besteht auch schon

```html
<!DOCTYPE html>
<html lang="de">
<head>
<meta charset="utf-8">
<title>Freie Gemeinde Lichtweg – Webdesign</title>
<link rel="stylesheet" href="https://fonts.googleapis.com/css2?family=Arimo:wght@400;700&family=Tinos:wght@400;700&display=swap">
<style>
:root{
  --canvas:#e6e4e6;
  --purple:#4e3660;
  --purple-mid:#7a6486;
  --purple-soft:#a596ad;
  --slate:#8f97a8;
  --slate-dark:#6f778a;
  --beige:#e4dcb4;
  --beige-dark:#c9bb7c;
  --ink:#2f2538;
  --gold-ink:#6d5a16;
  --white:#ffffff;
  --card-dark:#2c2630;
}
*{box-sizing:border-box;margin:0;padding:0}
html,body{width:1200px;height:1110px;overflow:hidden}
body{background:var(--canvas);font-family:"Arimo",Arial,sans-serif;color:var(--ink);position:relative}
.screen{position:absolute;width:360px;height:240px;overflow:hidden;background:var(--white);box-shadow:0 8px 22px rgba(60,50,70,.18)}
.screen--themen{left:30px;top:250px;background:linear-gradient(90deg,#f3efdd 0%,#fff 45%)}
.screen--literatur{left:420px;top:250px}
.screen--videos{left:810px;top:250px}
.screen--traktate{left:30px;top:530px}
.screen--home{left:420px;top:530px}
.screen--bibelkurs{left:810px;top:530px;background:var(--purple)}
.img{position:absolute;display:block}
.section-title{position:absolute;display:flex;align-items:center;font-weight:700;font-size:8px;letter-spacing:.02em;color:var(--ink)}
.section-title .mark{position:relative;width:24px;height:22px;margin-right:2px}
.section-title .mark i{position:absolute;width:15px;height:15px;border-radius:2px}
.section-title .mark i:first-child{left:0;top:0;opacity:.6}
.section-title .mark i:last-child{left:8px;top:7px}
.mark--beige i{background:var(--beige-dark)}
.mark--beige i:first-child{background:var(--beige)}
.mark--slate i{background:var(--slate-dark)}
.mark--slate i:first-child{background:var(--slate)}
.mark--purple i{background:var(--purple-mid)}
.mark--purple i:first-child{background:var(--purple-soft)}
.section-title--light{color:var(--white)}
.tiny{font-size:3.4px;line-height:1.5;color:#555}
.btn{position:absolute;background:var(--slate);color:#fff;font-size:3.5px;padding:2px 4px;border-radius:1px}

/* Literatur */
.book{position:absolute;top:50px;width:48px}
.book .cover{position:relative;height:78px;background:linear-gradient(180deg,#e9f0f6 0%,#6fa4cf 45%,#1f4f86 100%);box-shadow:1px 1px 3px rgba(0,0,0,.25)}
.book .tag{position:absolute;left:0;top:0;background:var(--purple);color:#fff;font-size:3.5px;padding:1px 3px}
.book .cover-title{position:absolute;left:4px;right:4px;top:18px;font-family:"Tinos",serif;font-size:5.5px;color:#8a2a2a;text-align:center;line-height:1.05}
.book p{font-size:2.8px;color:#555;margin-top:3px;line-height:1.4}

/* Videos */
.video-list{position:absolute;left:72px;top:80px;width:60px}
.video-list li{list-style:none;font-size:2.6px;color:#fff;padding:2.5px 3px;border-bottom:.5px solid rgba(255,255,255,.3)}
.video-list li:first-child{background:var(--slate)}
.footer{position:absolute;left:0;right:0;bottom:0;height:40px;background:var(--purple);color:#fff}
.footer .org{position:absolute;left:40px;top:7px;font-size:4px;font-weight:700;width:70px;text-align:center;line-height:1.2}
.field{position:absolute;height:7px;background:#fff;border-radius:2px;font-size:2.4px;color:#666;padding:2px 3px}
.contact{position:absolute;left:230px;top:6px;font-size:2.8px;line-height:1.4}

/* Traktate */
.tract-card{position:absolute;left:45px;top:30px;width:270px;height:155px;background:rgba(255,255,255,.93);border-radius:3px}
.tab-list li{list-style:none;font-size:2.6px;padding:3px;width:60px;color:var(--ink)}
.tab-list li:first-child{background:var(--slate);color:#fff}
.flags{position:absolute;left:95px;top:125px;display:flex;gap:7px}
.flags span{width:8px;height:6px;display:block}

/* Home */
.topbar{position:absolute;left:0;right:0;top:0;height:8px;background:var(--slate);color:#fff;font-size:2.6px}
.topbar .site{position:absolute;left:70px;top:2.5px}
.topbar .cta{position:absolute;left:240px;top:1.5px;background:var(--purple);border-radius:3px;padding:1px 5px;font-size:2.2px}
.nav{position:absolute;left:0;right:0;top:8px;height:10px;background:var(--purple);display:flex;justify-content:center;gap:5px;align-items:center}
.nav span{font-size:2.8px;color:#fff;letter-spacing:.03em}
.quote{position:absolute;left:150px;top:50px;width:128px;padding:6px 4px;background:rgba(110,84,130,.72);color:#fff;font-family:"Tinos",serif;font-size:5.2px;text-align:center;line-height:1.35}
.quote small{display:block;font-size:2.4px;text-align:right;margin-top:3px}
.welcome{position:absolute;left:90px;top:135px;width:190px;height:105px;background:#fff}
.welcome h2{font-size:6px;color:var(--gold-ink);line-height:1.1;margin:14px 0 2px 2px}
.welcome h2 em{font-style:normal;color:var(--purple)}

/* Bibelkurs */
.course-card{position:absolute;left:40px;top:35px;width:250px;height:120px;background:var(--card-dark);border-radius:4px}
.course-tabs{position:absolute;left:8px;top:45px;display:flex;gap:2px}
.course-tabs span{width:37px;height:7px;font-size:2.4px;color:#fff;background:var(--slate);padding:2px;border-radius:1px}
.course-tabs span:first-child{background:var(--purple)}
.booking{position:absolute;left:55px;top:162px;width:145px;height:40px;border:.5px solid var(--purple-soft);border-radius:3px;padding:4px}
.booking h4{font-size:3px;color:#fff;margin-bottom:2px}
.booking p{color:#ddd}
.accordion{position:absolute;left:55px;top:205px;width:145px;height:8px;background:var(--slate);font-size:2.6px;color:#fff;padding:2.5px 3px}
</style>
</head>
<body>

<!-- Themen -->
<section class="screen screen--themen">
  <h2 class="section-title" style="left:70px;top:10px"><span class="mark mark--beige"><i></i><i></i></span>THEMEN</h2>
  <div class="img" role="img" aria-label="Foto einer aufgeschlagenen alten Bibel auf einem Holztisch" style="left:72px;top:40px;width:190px;height:140px;border-radius:4px;background:radial-gradient(ellipse at 55% 55%,#d8c7a6 0%,#a58d6a 45%,#4a3e33 100%)"></div>
  <span class="btn" style="left:72px;top:188px">Mehr lesen</span>
</section>

<!-- Literatur -->
<section class="screen screen--literatur">
  <h2 class="section-title" style="left:78px;top:12px"><span class="mark mark--slate"><i></i><i></i></span>LITERATUR</h2>
  <div class="book" style="left:80px">
    <div class="cover" role="img" aria-label="Buchcover mit Boot auf ruhigem blauem Wasser"><span class="tag">Angebot!</span><span class="cover-title">WEGE ZUR INNEREN RUHE</span></div>
    <p>Wege zur inneren Ruhe – Band 1<br>4,50 € 0,00 €</p>
  </div>
  <div class="book" style="left:152px">
    <div class="cover" role="img" aria-label="Buchcover mit Boot auf ruhigem blauem Wasser"><span class="tag">Angebot!</span><span class="cover-title">WEGE ZUR INNEREN RUHE</span></div>
    <p>Wege zur inneren Ruhe – Band 2<br>4,50 € 0,00 €</p>
  </div>
  <div class="book" style="left:224px">
    <div class="cover" role="img" aria-label="Buchcover mit Boot auf ruhigem blauem Wasser"><span class="tag">Angebot!</span><span class="cover-title">WEGE ZUR INNEREN RUHE</span></div>
    <p>Wege zur inneren Ruhe – Band 3<br>4,50 € 0,00 €</p>
  </div>
  <svg class="img" width="360" height="50" style="left:0;bottom:0" viewBox="0 0 360 50" aria-hidden="true">
    <path d="M0 0 Q180 22 360 0 V50 H0Z" fill="#c9c0cf"/>
    <path d="M0 22 Q180 8 360 24 V50 H0Z" fill="#9a8ca3"/>
  </svg>
  <h2 class="section-title section-title--light" style="left:78px;top:222px"><span class="mark mark--purple"><i></i><i></i></span>VIDEOS</h2>
</section>

<!-- Videos -->
<section class="screen screen--videos">
  <div class="img" role="img" aria-label="Foto eines Holzkreuzes vor Bergen im Abendrot" style="left:0;top:0;width:360px;height:200px;background:linear-gradient(180deg,#9a97a8 0%,#b47a6e 30%,#d88a4a 48%,#3f3350 75%,#221d2c 100%)"></div>
  <h2 class="section-title section-title--light" style="left:75px;top:45px"><span class="mark mark--purple"><i></i><i></i></span>VIDEOS</h2>
  <ul class="video-list">
    <li>Stimmen unserer Zeit</li>
    <li>Der Name Gottes in der Prophetie</li>
    <li>Stimmen unserer Zeit – Folge 10</li>
  </ul>
  <div class="img" role="img" aria-label="Vorschaubild eines Videos mit Erdkugel und Titel Stimmen unserer Zeit" style="left:140px;top:78px;width:105px;height:62px;background:radial-gradient(circle at 50% 45%,#4d7fb0 0%,#1c2736 35%,#0c0c10 70%)"></div>
  <footer class="footer">
    <span style="position:absolute;left:28px;top:9px;width:8px;height:8px;background:var(--slate)"></span>
    <p class="org">FREIE GEMEINDE LICHTWEG E.V.</p>
    <span class="field" style="left:138px;top:5px;width:38px">Vorname</span>
    <span class="field" style="left:180px;top:5px;width:38px">Nachname</span>
    <span class="field" style="left:138px;top:15px;width:38px">E-Mail</span>
    <span class="field" style="left:180px;top:15px;width:38px">Telefon</span>
    <span class="field" style="left:138px;top:25px;width:80px">Ihre Nachricht an uns</span>
    <div class="contact">
      <svg width="4" height="5" viewBox="0 0 4 5" aria-hidden="true"><path d="M2 0a2 2 0 0 1 2 2c0 1.3-2 3-2 3S0 3.3 0 2a2 2 0 0 1 2-2z" fill="#fff"/></svg>
      <b>Postanschrift</b><br>FGL e.V.<br>Postfach 4411<br>10115 Berlin<br><b>E-Mail</b>
    </div>
  </footer>
</section>

<!-- Traktate -->
<section class="screen screen--traktate">
  <div class="img" role="img" aria-label="Foto eines Himmels mit Wolken im warmen Abendlicht" style="left:0;top:0;width:360px;height:240px;background:linear-gradient(180deg,#ece8e6 0%,#d9cfc5 50%,#a79b95 80%)"></div>
  <div class="img" aria-hidden="true" style="left:180px;top:0;width:180px;height:18px;background:var(--purple-mid)"></div>
  <div class="img" aria-hidden="true" style="left:0;top:185px;width:360px;height:55px;background:var(--purple)"></div>
  <div class="tract-card">
    <h2 class="section-title" style="left:35px;top:5px"><span class="mark mark--slate"><i></i><i></i></span>TRAKTATE</h2>
    <ul class="tab-list" style="position:absolute;left:0;top:45px">
      <li>Stimmen unserer Zeit</li>
      <li>Prophetie und Weltgeschehen</li>
      <li>Die Zehn Gebote im Vergleich</li>
      <li>Gesundheit</li>
    </ul>
    <div style="position:absolute;left:75px;top:48px;width:120px">
      <h3 style="font-size:4px;color:var(--purple);margin-bottom:2px">Stimmen unserer Zeit</h3>
      <p class="tiny">Ein Heft über die Zeichen der Zeit und den Weg des Glaubens. Es zeigt, wie die Bibel Ereignisse unserer Tage deutet, erklärt Prophetie in klaren Worten und lädt ein, Gottes Wort selbst zu prüfen. Viele Leser fanden darin Trost, Orientierung und neue Hoffnung für ihr Leben und ihre Familien.</p>
    </div>
    <div class="img" role="img" aria-label="Aufgefächerte gedruckte Traktate" style="left:200px;top:50px;width:55px;height:50px;background:linear-gradient(135deg,#f2e9e9 0%,#d8b0b0 60%,#b98a8a 100%)"></div>
    <div class="flags" aria-hidden="true">
      <span style="background:linear-gradient(#222 33%,#c22 33% 66%,#e8c12a 66%)"></span>
      <span style="background:linear-gradient(#c22 33%,#236 33% 66%,#e89a2a 66%)"></span>
      <span style="background:linear-gradient(#3a7bd5 33%,#222 33% 66%,#fff 66%)"></span>
      <span style="background:linear-gradient(#fff 40%,#2c5aa0 40% 60%,#fff 60%)"></span>
      <span style="background:linear-gradient(#fff 33%,#2c5aa0 33% 66%,#c22 66%)"></span>
      <span style="background:linear-gradient(#c22 50%,#fff 50%)"></span>
      <span style="background:linear-gradient(90deg,#2a8a3a 33%,#fff 33% 66%,#c22 66%)"></span>
      <span style="background:linear-gradient(#c22 25%,#e8c12a 25% 75%,#c22 75%)"></span>
      <span style="background:linear-gradient(#3a7bd5 50%,#e8c12a 50%)"></span>
    </div>
  </div>
</section>

<!-- Startseite -->
<section class="screen screen--home">
  <header class="topbar"><span class="site">FGL e.V. – freie christliche Gemeinde</span><span class="cta">JETZT BIBELKURS BUCHEN</span></header>
  <nav class="nav"><span>TRAKTATE</span><span>BIBELKURS</span><span>THEMEN</span><span>LITERATUR</span><span>VIDEOS</span><span>LINKS</span></nav>
  <div class="img" role="img" aria-label="Foto eines Sonnenuntergangs über ruhigem Wasser mit Lichtstrahlen durch Wolken" style="left:0;top:18px;width:360px;height:117px;background:radial-gradient(ellipse at 58% 45%,#f6dca0 0%,#c99658 25%,#6e5a4e 60%,#2f2a30 100%)"></div>
  <div class="img" role="img" aria-label="Gemeindeemblem mit offener Bibel" style="left:88px;top:50px;width:40px;height:55px;border-radius:4px;background:linear-gradient(180deg,#e9e6ee 0%,#b9b1c4 100%)"></div>
  <blockquote class="quote">SIEHE, ICH KOMME BALD UND MEIN LOHN MIT MIR, UM EINEN JEDEN SO ZU VERGELTEN, WIE SEIN WERK SEIN WIRD.<small>Offenbarung 22,12</small></blockquote>
  <div class="img" aria-hidden="true" style="left:180px;top:135px;width:180px;height:105px;background:var(--purple-mid)"></div>
  <article class="welcome">
    <span style="position:absolute;left:-4px;top:2px;width:14px;height:14px;background:var(--beige);border-radius:2px"></span>
    <h2>Liebe Besucher,<br><em>herzlich willkommen auf unserer Webseite!</em></h2>
    <p class="tiny" style="margin-left:2px">Die FGL e.V. ist eine freie christliche Gemeinde, die sich auf die biblischen Glaubenssätze stützt. Mit diesem Angebot möchten wir allen Suchenden einen Zugang zu Gottes Wort eröffnen und die Prophetie der Bibel verständlich erklären. Hier finden Sie Traktate, Bücher, Videos und einen kostenlosen Bibelkurs, der Sie Schritt für Schritt begleitet und Fragen unserer Zeit beantwortet.</p>
  </article>
</section>

<!-- Bibelkurs -->
<section class="screen screen--bibelkurs">
  <div class="img" aria-hidden="true" style="left:20px;top:0;width:320px;height:10px;background:#f1ece8;border-radius:0 0 3px 3px"></div>
  <div class="course-card">
    <div class="img" role="img" aria-label="Gedämpftes Foto einer aufgeschlagenen Bibel" style="left:0;top:0;width:250px;height:120px;border-radius:4px;background:linear-gradient(180deg,#2c2630 40%,#4a4040 100%)"></div>
    <h2 class="section-title section-title--light" style="left:30px;top:10px"><span class="mark mark--purple"><i></i><i></i></span>BIBELKURS</h2>
    <div class="course-tabs"><span>Einführung</span><span>Die Bibel</span><span>Das Gebet</span><span>Satan unser Feind</span><span>Jesus unser Freund</span><span>Die Wiedergeburt</span></div>
    <div style="position:absolute;left:12px;top:58px;width:225px">
      <p class="tiny" style="color:#eee">Einführung</p>
      <p class="tiny" style="color:#ccc">Dieser Kurs führt in kurzen Lektionen durch die wichtigsten Themen der Heiligen Schrift. Jede Lektion enthält Fragen, die Sie mit der Bibel in der Hand selbst beantworten. Wir prüfen Ihre Antworten gern und senden Ihnen danach die nächste Lektion zu, ganz ohne Kosten oder Verpflichtung.</p>
    </div>
    <span class="btn" style="left:12px;top:102px">Mehr erfahren</span>
  </div>
  <div class="booking">
    <h4>Bibelfernkurs buchen</h4>
    <p class="tiny">Lieber Leser, dieser Kurs ist kostenlos. Tragen Sie Ihre Daten ein und wählen Sie, ob Sie online oder per Post lernen möchten. Wir freuen uns auf Sie.</p>
  </div>
  <div class="accordion">Online</div>
  <div class="img" role="img" aria-label="Foto einer Person, die in einer Bibel liest" style="left:210px;top:162px;width:70px;height:55px;background:linear-gradient(135deg,#b59a82 0%,#5e6f8e 50%,#2f3446 100%)"></div>
</section>

</body>
</html>
```